Quillforge new logo business card

We need a business card designed to promote the new direction of our company. Originally (for the past 12 years) we were a design-based marketing consultancy specialising in B2B. But now we are offering marketing consultancy to companies in the ecommerce business. We have expertise in this and operate three online stores ourselves and can provide warehousing and distribution services.
The new logo and business card should reflect this market - e.g. modern, technical, commercial but also creative!
Our current logo is too 'designery' and doesn't reflect the seriousness and professionalism of our current business. It also is very long and thin so doesnot work well in rectangular panels.
The name 'Quillforge' comprises two parts - Quill and Forge and these parts of the word can have a different type font or colour. The 'Quill' element is the creative element while the 'Forge' part is the technical, businesslike part. We can also look at 'The Quillforge Company' rather than just 'quillforge.' We can also include the slogan 'Source, Sell, Succeed.' under the logo.
The address details for the card are 7 Larchmere Rise, Woking, Surrey RH14 3TN. We will also need an email address and phone number (details will be supplied later)
On the back of the card will be a list of services offered.
Quillforge can help your business succeed through:
Product Sourcing
Marketing
Distribution
Storage
Ecommerce

Target Market(s)

Owners of small and medium-sized retail businesses - particularly mail order and ecommerce based businesses.

Industry/Entity Type

Marketing

Requirements
Must have
• The company name should be prominent. This can either be 'Quillforge' or 'The Quillforge Company'.
• Then the words 'Quillforge Ltd, Unit F, Ashcombe Trade Park, Millrace Way, Ashcombe, Woking, Surrey RH17 9LW
• 0844 312 5809 www.thequillforge-example.co.uk
• Must also include cardholder's name and title.
• Gideon Halbrook
• Director
• On the reverse it should say.
• Quillforge - Developing profitable brands in a multi-channel environment

```html
<!DOCTYPE html>
<html lang="en">
<head>
<meta charset="utf-8">
<title>Quillforge – Business Card</title>
<link rel="stylesheet" href="https://fonts.googleapis.com/css2?family=Open+Sans:wght@400;700&display=swap">
<style>
  :root {
    --page-bg: #e9e9ec;
    --card-white: #ffffff;
    --card-shade: #eeeeef;
    --brand-indigo: #3d3f9f;
    --brand-sky: #00aeef;
    --ink: #3a3a3a;
    --icon: #3d3f9f;
  }
  * { margin: 0; padding: 0; box-sizing: border-box; }
  html, body { width: 1200px; height: 900px; overflow: hidden; }
  body {
    background: var(--page-bg);
    font-family: "Open Sans", Arial, sans-serif;
    color: var(--ink);
    position: relative;
  }
  .business-card {
    position: absolute;
    left: 92px; top: 160px;
    width: 1016px; height: 580px;
    border-radius: 44px;
    overflow: hidden;
    background: radial-gradient(ellipse at 40% 40%, var(--card-white) 45%, var(--card-shade) 100%);
    box-shadow: 0 6px 24px rgba(0,0,0,0.12);
  }
  .card-swoosh { position: absolute; inset: 0; width: 100%; height: 100%; }
  .wordmark {
    position: absolute;
    left: 62px; top: 64px;
    font-family: "Open Sans", Arial, sans-serif;
    font-weight: 700;
    font-size: 62px;
    line-height: 1;
    color: var(--brand-indigo);
  }
  .contact-list {
    position: absolute;
    left: 56px; top: 250px;
    list-style: none;
    font-size: 21px;
    line-height: 30px;
  }
  .contact-list li { display: flex; align-items: flex-start; gap: 10px; }
  .contact-icon { width: 20px; height: 20px; margin-top: 5px; flex: none; }
  .cardholder {
    position: absolute;
    left: 540px; top: 392px;
    width: 250px;
    text-align: right;
  }
  .cardholder-name { font-weight: 700; font-size: 28px; color: var(--brand-indigo); line-height: 36px; }
  .cardholder-title { font-size: 25px; color: var(--ink); line-height: 32px; }
</style>
</head>
<body>
  <div class="business-card">
    <svg class="card-swoosh" viewBox="0 0 1016 580" aria-hidden="true">
      <path d="M440,580 C700,540 890,430 940,230 L1030,230 L1030,590 Z" fill="var(--brand-sky)"/>
      <path d="M850,-10 C1000,170 950,440 610,590 L1030,590 L1030,-10 Z" fill="var(--brand-indigo)" stroke="var(--card-white)" stroke-width="7"/>
    </svg>

    <div class="wordmark">Quillforge</div>

    <ul class="contact-list">
      <li>
        <svg class="contact-icon" viewBox="0 0 20 20"><circle cx="10" cy="10" r="10" fill="var(--icon)"/><path d="M10 4a4 4 0 0 0-4 4c0 3 4 8 4 8s4-5 4-8a4 4 0 0 0-4-4z" fill="#fff"/><circle cx="10" cy="8" r="1.5" fill="var(--icon)"/></svg>
        <span>Quillforge Ltd, Unit F, Ashcombe Trade Park,<br>Millrace Way, Ashcombe, Woking,<br>Surrey RH17 9LW</span>
      </li>
      <li>
        <svg class="contact-icon" viewBox="0 0 20 20"><circle cx="10" cy="10" r="10" fill="var(--icon)"/><path d="M6 5l2.5-.5 1.2 3-1.5 1a7 7 0 0 0 3.3 3.3l1-1.5 3 1.2-.5 2.5C10 14 6 10 6 5z" fill="#fff"/></svg>
        <span>0844 312 5809</span>
      </li>
      <li>
        <svg class="contact-icon" viewBox="0 0 20 20"><circle cx="10" cy="10" r="10" fill="var(--icon)"/><rect x="7" y="4" width="6" height="12" rx="1.2" fill="#fff"/><rect x="8" y="5.5" width="4" height="7" fill="var(--icon)"/></svg>
        <span>07700 900418</span>
      </li>
      <li>
        <svg class="contact-icon" viewBox="0 0 20 20"><circle cx="10" cy="10" r="10" fill="var(--icon)"/><rect x="5" y="8" width="10" height="6" rx="1" fill="#fff"/><rect x="7" y="5" width="6" height="3" fill="#fff"/></svg>
        <span>0844 312 5810</span>
      </li>
      <li>
        <svg class="contact-icon" viewBox="0 0 20 20"><circle cx="10" cy="10" r="10" fill="var(--icon)"/><rect x="5" y="6.5" width="10" height="7" fill="#fff"/><path d="M5 6.5l5 4 5-4" fill="none" stroke="var(--icon)" stroke-width="1.2"/></svg>
        <span>gideon@thequillforge-example.co.uk</span>
      </li>
      <li>
        <svg class="contact-icon" viewBox="0 0 20 20"><circle cx="10" cy="10" r="10" fill="var(--icon)"/><circle cx="10" cy="10" r="5.5" fill="none" stroke="#fff" stroke-width="1.3"/><ellipse cx="10" cy="10" rx="2.3" ry="5.5" fill="none" stroke="#fff" stroke-width="1.1"/><path d="M4.5 10h11" stroke="#fff" stroke-width="1.1"/></svg>
        <span>www.thequillforge-example.co.uk</span>
      </li>
    </ul>

    <div class="cardholder">
      <p class="cardholder-name">Gideon Halbrook</p>
      <p class="cardholder-title">Director</p>
    </div>
  </div>
</body>
</html>
```